Flyer-Design für massive Tiny-Häuser eines Hausherstellers
Zielgruppe
Die Wohnfeld Bau GmbH ist der Haushersteller in Deutschland, mit einem Angebot „nachhaltiger“ Ausbauhäuser. Ein nachhaltiges Gebäude zeichnet sich durch
seine hohe ökologische und ökonomische Qualität aus. Der Aspekt möglichst chemiefrei zu bauen steht hier im Vordergrund. Ein faires Preisleistungsverhältnis, persönliche Beratung, der ökologische Baustoff Porenbeton und die Zusammenarbeit mit deutschen Herstellern und Marktführern, ermöglichen es uns Ihnen ein passgenaues Angebot zu machen.
Individuell – Nachhaltig – Massiv
Mit dem Ausbauhaus der Wohnfeld Bau GmbH, erwerben die Bauherren einen veredelten Rohbau, das heißt: Bodenplatte, Mauerwerk, Dach inklusive Dacheindeckung, Fenster und Tür.
Durch eine transparente Kostenaufstellung der Gewerke kann der Bauherr nun entscheiden, ob er durch Eigenleistung (die sogenannte „Muskelhypothek) enorme Kosten sparen möchte/kann, oder die weiteren Ausbauleistungen an Handwerksunternehmen vergeben möchte. Beispielhaft seien hier der Trockenbau, aber auch Elektro- und Sanitärinstallationen genannt.
Markus Velten, Gründer der Wohnfeld Bau GmbH ist seit vielen Jahren im Hausbau tätig und hat es sich zur Aufgabe gemacht ein völlig neues Hausbaukonzept zu entwickeln, dass seine Kunden ein Stück weit unabhängiger von den Finanzierungen der Banken macht, in dem die Möglichkeit der Eigenleistung stärker in den Blickpunkt rückt.
Aufgrund des enormen Preisanstieges bei den Grundstücken in Deutschland, wurde es vielen Menschen fast unmöglich den Traum vom Eigenheim zu verwirklichen, da das Budget für den eigentlichen Hausbau auf der Strecke blieb.
Das Konzept „Wohnfeld Bau“ wurde geboren. Gemeinsam mit Freunden und Geschäftspartnern, wurde aus der Idee individuellen Wohnraum zu schaffen, der mit nachhaltigen und ökologischen Baustoffen massiv gebaut, jedoch aufgrund der Möglichkeit Eigenleistung einzubringen, finanzierbar bleibt, Wirklichkeit.
Aufgabenstellung
Wir brauchen ein modernes und dynamisches design was sich an den Farben aus unserem Logo anlehnt.
Der Flyer soll für unsere KORVA Häuser sein. Das sind massive Tiny Häuser mit 50 und 70 qm.
Texte werden wir dann zur Verfügung stellen. Anhalt sind aber schon mal die Bilder di wir hochgeladen haben.
Ziel soll es sein das wir eine Flyer machen für die Bausätze mit den Schlagwörtern wie auf dem werbe Bild beschrieben.

```html
<!DOCTYPE html>
<html lang="de">
<head>
<meta charset="utf-8">
<title>Wohnfeld Bau – Flyer KORVA 70</title>
<link rel="stylesheet" href="https://fonts.googleapis.com/css2?family=Montserrat:wght@400;500;700&display=swap">
<style>
  :root{
    --orange:#e8793a;
    --ink:#3b3b3b;
    --sky:#7aa9c3;
    --paper:#ffffff;
    --stage:#ececec;
  }
  *{box-sizing:border-box;margin:0;padding:0}
  html,body{width:1200px;height:1083px;overflow:hidden;background:var(--stage);font-family:"Montserrat",sans-serif;color:var(--ink)}
  .canvas{position:relative;width:1200px;height:1083px}
  .page{position:absolute;top:160px;width:540px;height:764px;background:var(--paper);overflow:hidden}
  .page--back{left:40px}
  .page--front{left:620px}
  .frame{position:absolute;inset:20px;border:1px solid var(--orange);pointer-events:none;z-index:5}

  .banner{position:absolute;background:var(--orange);color:var(--ink);white-space:nowrap;transform:rotate(-5deg);transform-origin:left bottom;z-index:4}
  .banner--title{font-weight:700;font-size:23px;padding:6px 10px 6px 14px}
  .banner--price{font-weight:400;font-size:21px;padding:6px 12px 6px 14px}

  .included{position:absolute;font-size:11.5px;line-height:1.45;z-index:4}
  .included h3{font-size:11.5px;font-weight:700;margin-bottom:6px}
  .included li{list-style:none}

  .photo{position:absolute}
  .photo--garden{background:linear-gradient(180deg,#8fb4cc 0%,#9dbcd0 22%,#4d6a32 42%,#3b5326 62%,#5d7d33 78%,#4a6a28 100%)}
  .plan{position:absolute;background:linear-gradient(135deg,#f4f4f4,#e3e3e3);border:1px solid #cfcfcf}

  .copy{position:absolute;font-size:9.5px;line-height:1.45;text-align:justify}
  .copy h4{font-size:10.5px;font-weight:700;margin-bottom:10px;text-align:left}
  .copy p+p{margin-top:10px}

  .brand{position:absolute;display:flex;align-items:center;gap:8px;z-index:4}
  .brand__mark{width:12px;height:12px;background:var(--orange)}
  .brand__name{font-weight:500;font-size:18px;color:var(--orange);letter-spacing:.5px}

  .contact{position:absolute;left:40px;right:40px;font-size:8.5px;font-weight:700;color:var(--orange);text-align:center;line-height:1.6;z-index:4}
  .contact svg{width:9px;height:9px;vertical-align:-1px;margin-right:2px}

  .page--front .sky{position:absolute;left:0;top:0;width:540px;height:230px;background:var(--sky)}
  .page--front .footer-band{position:absolute;left:0;top:576px;width:540px;height:188px;background:var(--paper)}
</style>
</head>
<body>
<main class="canvas">

  <!-- Rückseite -->
  <section class="page page--back">
    <div class="frame"></div>
    <div class="banner banner--title" style="left:28px;top:94px">Massives Tiny Haus KORVA 70</div>
    <div class="banner banner--price" style="left:28px;top:132px">Bausatzhaus ab 44.900€</div>

    <div class="included" style="left:56px;top:186px">
      <h3>Enthalten im Bausatz:</h3>
      <ul>
        <li>- Wandpaket aus Porenbeton</li>
        <li>- Fenster</li>
        <li>- Dasch aus Porenbeton</li>
        <li>- Dachabdichtung</li>
        <li>- Bauanleitung</li>
        <li>- Lieferung zur Baustelle</li>
      </ul>
    </div>

    <div class="photo photo--garden" role="img" aria-label="Gartenansicht des Tiny Hauses zwischen Bäumen" style="left:320px;top:150px;width:220px;height:170px"></div>

    <div class="plan" role="img" aria-label="Grundriss des Tiny Hauses KORVA 70" style="left:50px;top:350px;width:210px;height:200px"></div>

    <div class="copy" style="left:290px;top:340px;width:215px">
      <h4>Lorem ipsum dolor</h4>
      <p>sit amet, consectetuer adipiscing elit, sed diam nonummy nibh euismod tincidunt ut laoreet dolore magna aliquam erat volutpat. Ut wisi enim ad minim veniam.</p>
      <p>Ut wisi enim ad minim veniam, quis nostrud exerci tation ullamcorper suscipit lobortis nisl ut aliquip ex ea commodo consequat. Duis autem vel eum iriure dolor in hendrerit.</p>
    </div>

    <div class="photo photo--garden" role="img" aria-label="Seitenansicht des Hauses mit Bäumen und Blüten" style="left:340px;top:525px;width:200px;height:120px"></div>

    <div class="copy" style="left:50px;top:580px;width:250px">
      <h4>Lorem ipsum dolor</h4>
      <p>sit amet, consectetuer adipiscing elit, sed diam nonummy nibh euismod tincidunt ut laoreet dolore magna aliquam erat volutpat. Ut wisi enim ad minim veniam.</p>
    </div>

    <div class="brand" style="left:300px;top:672px">
      <span class="brand__mark"></span><span class="brand__name">Wohnfeld Bau</span>
    </div>

    <div class="contact" style="top:706px">
      Wohnfeld Bau GmbH Talweg 18 41061 Mönchengladbach<br>
      <svg viewBox="0 0 10 10"><path d="M2 1l2 2-1 1.5c.7 1.3 1.2 1.8 2.5 2.5L7 6l2 2-1.5 1.5C4 9 1 6 .5 2z" fill="none" stroke="currentColor" stroke-width=".9"/></svg>0 21 61 / 48 30 110 |
      <svg viewBox="0 0 10 10"><path d="M1 5l8-4-3 8-1.5-3z" fill="none" stroke="currentColor" stroke-width=".9"/></svg>info@wohnfeld-bau.de
    </div>
  </section>

  <!-- Vorderseite -->
  <section class="page page--front">
    <div class="sky"></div>
    <div class="photo photo--garden" role="img" aria-label="Tiny Haus KORVA 70 mit Terrasse, Garten und Bäumen" style="left:0;top:200px;width:540px;height:376px"></div>
    <div class="footer-band"></div>
    <div class="frame"></div>

    <div class="brand" style="left:44px;top:46px">
      <span class="brand__mark"></span><span class="brand__name">Wohnfeld Bau</span>
    </div>

    <div class="banner banner--title" style="left:14px;top:150px">Massives Tiny Haus KORVA 70</div>
    <div class="banner banner--price" style="left:14px;top:190px">Bausatzhaus ab 44.900€</div>

    <div class="included" style="left:330px;top:160px">
      <h3>Enthalten im Bausatz:</h3>
      <ul>
        <li>- Wandpaket aus Porenbeton</li>
        <li>- Fenster</li>
        <li>- Dasch aus Porenbeton</li>
        <li>- Dachabdichtung</li>
        <li>- Bauanleitung</li>
        <li>- Lieferung zur Baustelle</li>
      </ul>
    </div>

    <div class="copy" style="left:44px;top:592px;width:210px">
      <h4>Lorem ipsum dolor</h4>
      <p>sit amet, consectetuer adipiscing elit, sed diam nonummy nibh euismod tincidunt ut laoreet dolore magna aliquam erat volutpat. Ut wisi enim ad minim veniam, quis nostrud exerci tation ullamcorper suscipit lobortis nisl ut aliquip ex ea</p>
    </div>
    <div class="copy" style="left:282px;top:614px;width:214px">
      <p>Ut wisi enim ad minim veniam, quis nostrud exerci tation ullamcorper suscipit lobortis nisl ut aliquip ex ea commodo consequat. Duis autem vel eum iriure dolor in hendrerit.</p>
      <p>Lorem ipsum dolor sit amet, consectetuer adipiscing elit.</p>
    </div>

    <div class="contact" style="top:714px">
      Wohnfeld Bau GmbH Talweg 18 41061 Mönchengladbach<br>
      <svg viewBox="0 0 10 10"><path d="M2 1l2 2-1 1.5c.7 1.3 1.2 1.8 2.5 2.5L7 6l2 2-1.5 1.5C4 9 1 6 .5 2z" fill="none" stroke="currentColor" stroke-width=".9"/></svg>0 21 61 / 48 30 110 |
      <svg viewBox="0 0 10 10"><path d="M1 5l8-4-3 8-1.5-3z" fill="none" stroke="currentColor" stroke-width=".9"/></svg>info@wohnfeld-bau.de |
      <svg viewBox="0 0 10 10"><rect x="1" y="1.5" width="8" height="5.5" fill="none" stroke="currentColor" stroke-width=".9"/><path d="M3 9h4" stroke="currentColor" stroke-width=".9"/></svg>www.wohnfeld-bau.de
    </div>
  </section>

</main>
</body>
</html>
```